Fairway Circuit web site

Fairway Circuit is a High End golf amateur Tour targeted to wealthy golf passionates.
The concept is to take average golfers and offer them the same playing conditions than the pros (Caddies, branded bags, TV coverage...) and bring them to the most beautiful golf courses around the world.
Keywords: International, Exclusive, Luxury, but not show-off...
The Task is to design the WordPress template and a exemple page.
Please use the provided logo and any stock image you like.
Updates

Hello,

please note that the outcome has to be a fully coded WordPress site.

Please no "Photoshop only" designs...

Thanks

```html
<!DOCTYPE html>
<html lang="en">
<head>
<meta charset="utf-8">
<title>Fairway Circuit</title>
<link rel="stylesheet" href="https://fonts.googleapis.com/css2?family=Open+Sans:wght@400;600;700&display=swap">
<style>
:root{
  --green-dark:#1d5538;
  --green-title:#1e5e3d;
  --orange:#d99a2a;
  --orange-text:#d08a14;
  --grass:#2f6e2a;
  --grass-dark:#245a21;
  --grey-bg:#f2f2f2;
  --grey-text:#7a7a7a;
  --light-text:#a0a0a0;
  --line:#dcdcdc;
  --white:#ffffff;
  --ink:#333333;
}
*{box-sizing:border-box;margin:0;padding:0}
html,body{width:1200px;height:2647px;overflow:hidden}
body{font-family:"Open Sans",Arial,sans-serif;color:var(--ink);background:var(--white);position:relative}
.abs{position:absolute}
.photo{position:absolute;display:block}

/* top bar */
.topbar{position:absolute;left:0;top:0;width:1200px;height:48px;background:var(--green-dark)}
.topbar .social{position:absolute;left:130px;top:15px;display:flex;gap:9px}
.topbar .social span{width:17px;height:17px;border-radius:50%;background:#3f8a5c}
.toplinks{position:absolute;left:376px;top:14px;display:flex;gap:0;font-size:13px;color:var(--white)}
.toplinks a{color:var(--white);text-decoration:none;margin-right:27px}
.other-tours{position:absolute;left:946px;top:10px;width:123px;height:28px;border:1px solid #9fbfae;border-radius:3px;color:var(--white);font-size:13px;line-height:26px;padding-left:12px}
.other-tours svg{position:absolute;right:12px;top:10px}

/* header */
.header{position:absolute;left:0;top:48px;width:1200px;height:91px;background:var(--orange)}
.brand{position:absolute;left:132px;top:24px;display:flex;align-items:center;gap:10px;color:var(--white);font-size:16px;font-weight:700}
.brand .dot{width:42px;height:42px;border-radius:50%;background:var(--green-dark)}
.nav{position:absolute;left:311px;top:34px;display:flex;font-size:15px;color:var(--white)}
.nav a{color:var(--white);text-decoration:none;margin-right:35px;position:relative}
.nav a.active{color:var(--green-dark)}
.nav a.active::after{content:"";position:absolute;left:0;right:0;top:57px;height:3px;background:var(--green-dark)}

/* hero */
.hero{position:absolute;left:0;top:139px;width:1200px;height:518px;background:linear-gradient(180deg,var(--grass),var(--grass-dark))}
.hero-frame{position:absolute;left:132px;top:39px;width:936px;height:434px;background:var(--white)}
.arrow-btn{position:absolute;width:28px;height:28px}
.save{position:absolute;left:763px;top:395px;font-size:35px;font-weight:700;color:var(--white);letter-spacing:0.5px}

/* welcome */
.welcome-title{position:absolute;left:131px;top:680px;font-size:37px;font-weight:700;color:var(--green-title)}
.welcome-sub{position:absolute;left:131px;top:1006px;font-size:15px;color:var(--grey-text)}
.welcome-copy{position:absolute;left:131px;top:1038px;width:480px;font-size:11px;line-height:19px;color:var(--grey-text)}
.btn{position:absolute;background:linear-gradient(#fafafa,#e2e2e2);border:1px solid #d0d0d0;border-radius:2px;font-size:10px;color:#555;text-align:center}
.tab{position:absolute;height:41px;line-height:39px;background:linear-gradient(#fafafa,#e4e4e4);border:1px solid #d2d2d2;border-radius:2px;font-size:10px;color:#555;text-align:center}
.tab.on{background:linear-gradient(#d8d8d8,#c8c8c8);color:var(--green-dark)}
.news{position:absolute;left:655px;width:413px}
.news .thumb{position:absolute;left:0;top:0;width:113px;height:96px;border:1px solid var(--line);padding:5px;background:var(--white)}
.news .thumb div{width:100%;height:100%}
.news h3{position:absolute;left:139px;top:0;font-size:13px;font-weight:400;color:var(--orange-text);white-space:nowrap}
.news .date{position:absolute;left:139px;top:30px;font-size:10px;color:var(--light-text)}
.news p{position:absolute;left:139px;top:52px;width:275px;font-size:11px;line-height:20px;color:var(--light-text)}
.news p a{color:var(--green-dark);font-weight:600;text-decoration:underline}
.rule{position:absolute;height:1px;background:var(--line)}

/* featured */
.featured{position:absolute;left:0;top:1244px;width:1200px;height:335px;background:var(--grey-bg);border-top:1px solid #e6e6e6}
.section-title{position:absolute;left:0;width:1200px;text-align:center;font-size:19px;color:var(--green-title)}
.card{position:absolute;width:208px}
.card .pic{width:208px;height:164px;border:1px solid #e0e0e0}
.card .name{font-size:14px;color:#444;margin-top:14px}
.card .meta{font-size:12px;color:var(--light-text);margin-top:3px}
.play{position:absolute;left:50%;top:50%;margin:-20px 0 0 -20px}

/* players */
.player{position:absolute;width:300px}
.player .face{position:absolute;left:0;top:0;width:113px;height:113px;border-radius:50%}
.player .flag{position:absolute;left:131px;top:22px}
.player .pname{position:absolute;left:162px;top:18px;font-size:14px;color:#444}
.player .pcopy{position:absolute;left:131px;top:44px;width:170px;font-size:11px;line-height:19px;color:var(--light-text)}
.player .pct{position:absolute;left:131px;top:85px;font-size:27px;font-weight:700;color:var(--orange-text)}
.slide{position:absolute;width:28px;height:28px;border:1px solid var(--line);background:#f6f6f6}
.slide svg{position:absolute;left:9px;top:8px}

/* video grid */
.vcard{position:absolute;width:208px}
.vcard .pic{width:208px;height:196px;position:relative}
.vcard .cap{font-size:14px;line-height:21px;color:#555;margin-top:8px}
.vcard .meta{font-size:12px;color:var(--light-text);margin-top:3px}

/* partners */
.partners{position:absolute;left:0;top:2277px;width:1200px;height:208px;border-top:1px solid #e6e6e6}
.badge{position:absolute}

/* footer */
.footer{position:absolute;left:0;top:2485px;width:1200px;height:162px;background:linear-gradient(180deg,var(--grass),var(--grass-dark))}
.footer .links{position:absolute;left:132px;top:50px;font-size:13px;color:var(--white)}
.footer .links a{color:var(--white);text-decoration:none;margin-right:20px}
.footer .copy{position:absolute;left:132px;top:93px;font-size:11px;color:var(--white)}
.footer .social{position:absolute;left:771px;top:60px;display:flex;gap:10px}
.footer .social span{width:39px;height:39px;border-radius:50%;background:var(--white)}
.footer .brand-foot{position:absolute;left:940px;top:66px;display:flex;align-items:center;gap:8px;color:var(--white);font-size:14px;font-weight:700}
.footer .brand-foot .dot{width:30px;height:30px;border-radius:50%;background:var(--green-dark);border:2px solid var(--white)}
</style>
</head>
<body>

<div class="topbar">
  <div class="social"><span></span><span></span><span></span><span></span><span></span><span></span></div>
  <nav class="toplinks"><a>Meridian Tour</a><a>Pro Shop</a><a>Ladies Links Foundation</a><a>Teaching &amp; Club Pros</a><a>Girls Golf</a></nav>
  <div class="other-tours">Other Tours:
    <svg width="9" height="7" viewBox="0 0 9 7"><path d="M0 0h9L4.5 7z" fill="#fff"/></svg>
  </div>
</div>

<header class="header">
  <div class="brand"><span class="dot"></span>Fairway Circuit</div>
  <nav class="nav">
    <a class="active">HOME</a><a>ABOUT US</a><a>SERVICES</a><a>VIDEOS</a><a>BLOG</a><a>NEWS</a><a>TESTIMONIALS</a><a>CONTACT US</a>
  </nav>
</header>

<section class="hero">
  <div class="hero-frame">
    <div class="photo" role="img" aria-label="Golfer mid swing on a green fairway with hills" style="left:3px;top:3px;width:581px;height:428px;background:linear-gradient(180deg,#7fb4e0 0%,#b9d6ea 30%,#5f8f3a 48%,#6fa13c 100%)"></div>
    <svg class="arrow-btn" style="left:10px;top:199px" viewBox="0 0 28 28"><circle cx="14" cy="14" r="12" fill="none" stroke="#fff" stroke-width="2"/><path d="M16 8l-6 6 6 6" fill="none" stroke="#fff" stroke-width="2.5"/></svg>
    <svg class="arrow-btn" style="left:549px;top:199px" viewBox="0 0 28 28"><circle cx="14" cy="14" r="12" fill="none" stroke="#fff" stroke-width="2"/><path d="M12 8l6 6-6 6" fill="none" stroke="#fff" stroke-width="2.5"/></svg>
    <div class="photo" role="img" aria-label="Driver head beside a ball on a tee in grass" style="left:587px;top:3px;width:346px;height:211px;background:linear-gradient(180deg,#c9d98a 0%,#7fa83a 50%,#4d7d22 100%)">
      <svg class="play" width="40" height="40" viewBox="0 0 40 40"><circle cx="20" cy="20" r="17" fill="none" stroke="#fff" stroke-width="2.5"/><path d="M16 12l11 8-11 8z" fill="#fff"/></svg>
    </div>
    <div class="photo" role="img" aria-label="Silhouette of a golfer against a golden sunset" style="left:587px;top:219px;width:346px;height:212px;background:radial-gradient(circle at 50% 40%,#f4d36a 0%,#d9962a 55%,#8a5a18 100%)"></div>
    <div class="save" style="left:632px;top:357px">SAVE $ 20 OFF</div>
  </div>
</section>

<h1 class="welcome-title">WELCOME!</h1>
<div class="photo" role="img" aria-label="Close-up of a golf ball on a red tee in grass" style="left:131px;top:741px;width:476px;height:246px;background:radial-gradient(circle at 42% 40%,#f4f4f2 0%,#e8ece2 20%,#8fbf4a 40%,#4f8a22 100%)"></div>
<h2 class="welcome-sub">GOLF IS LIKE LIFE! BUT IT IS MORE COMPLICATED THAN THAT</h2>
<p class="welcome-copy">Lorem ipsum dolor sit amet, consectetuer adipiscing elit, sed diam nonummy nibh euismod tin cidunt ut laoreet dolore magna aliquam erat volutpat. Ut wisi enim ad minim veniam, quis nos trud exerci tation ullamcorper suscipit lobortis nisl ut aliquip ex ea commodo consequat. Duis trud exerci tation ullamcorper suscipit lobortis nisl ut aliquip ex ea commodo consequat. Duis autem vel eum iriure dolorn hendrerit in vulputate velit esse molestie conse.</p>
<div class="btn" style="left:131px;top:1175px;width:57px;height:27px;line-height:25px">MORE</div>

<div class="tab on" style="left:653px;top:690px;width:110px">LATEST NEWS</div>
<div class="tab" style="left:768px;top:690px;width:110px">RECENT NEWS</div>
<div class="tab" style="left:883px;top:690px;width:111px">COMMENTS</div>

<article class="news" style="top:762px">
  <div class="thumb"><div role="img" aria-label="Golf ball and club on a green" style="background:linear-gradient(180deg,#8ec0e6,#5e9a32)"></div></div>
  <h3>Nemo enim ipsam voluptatem quia voluptas</h3>
  <div class="date">12-09-2014</div>
  <p>Lorem ipsum dolor sit amet, consectetuer adipi ing elit, sed diam nonummy. <a>Read More</a></p>
</article>
<div class="rule" style="left:655px;top:893px;width:413px"></div>
<article class="news" style="top:919px">
  <div class="thumb"><div role="img" aria-label="Golfer finishing a swing" style="background:linear-gradient(180deg,#9fb7cf,#3c4d6a)"></div></div>
  <h3>Nemo enim ipsam voluptatem quia voluptas</h3>
  <div class="date">12-09-2014</div>
  <p>Lorem ipsum dolor sit amet, consectetuer adipi ing elit, sed diam nonummy. <a>Read More</a></p>
</article>
<div class="rule" style="left:655px;top:1048px;width:413px"></div>
<article class="news" style="top:1069px">
  <div class="thumb"><div role="img" aria-label="Golfer in a cap on the course" style="background:linear-gradient(180deg,#a8c6b0,#5a8a52)"></div></div>
  <h3>Nemo enim ipsam voluptatem quia voluptas</h3>
  <div class="date">12-09-2014</div>
  <p>Lorem ipsum dolor sit amet, consectetuer adipi ing elit, sed diam nonummy. <a>Read More</a></p>
</article>
<div class="rule" style="left:655px;top:1200px;width:413px"></div>

<section class="featured">
  <h2 class="section-title" style="top:26px">FEATURED CONTENT</h2>
  <div class="card" style="left:132px;top:78px">
    <div class="pic" role="img" aria-label="Putter next to a ball on the green" style="background:linear-gradient(180deg,#5e9a3a,#3f7a22)"></div>
    <div class="name">CALLUM REYES</div><div class="meta">Fine form at Cedarbrook</div>
  </div>
  <div class="card" style="left:374px;top:78px">
    <div class="pic" role="img" aria-label="Golfer playing out of a bunker" style="position:relative;background:linear-gradient(180deg,#8aa35a,#c9b48a)"><svg class="play" width="40" height="40" viewBox="0 0 40 40"><circle cx="20" cy="20" r="17" fill="none" stroke="#fff" stroke-width="2.5"/><path d="M16 12l11 8-11 8z" fill="#fff"/></svg></div>
    <div class="name">FIRST LOOK</div><div class="meta">Fine form at Cedarbrook</div>
  </div>
  <div class="card" style="left:614px;top:78px">
    <div class="pic" role="img" aria-label="Portrait of a tour player in a cap" style="background:linear-gradient(180deg,#dfe6ea,#b9c6cc)"></div>
    <div class="name">CALLUM REYES</div><div class="meta">Fine form at Cedarbrook</div>
  </div>
  <div class="card" style="left:858px;top:78px">
    <div class="pic" role="img" aria-label="Club and ball on a tee under blue sky" style="background:linear-gradient(180deg,#7fb0dd 0%,#b9d3e6 45%,#5f9a30 60%,#3f7a20 100%)"></div>
    <div class="name">FIRST LOOK</div><div class="meta">Fine form at Cedarbrook</div>
  </div>
</section>

<div class="rule" style="left:131px;top:1624px;width:365px"></div>
<div class="rule" style="left:704px;top:1624px;width:364px"></div>
<h2 class="section-title" style="top:1612px">MEET THE PLAYERS</h2>

<div class="slide" style="left:88px;top:1715px"><svg width="8" height="10" viewBox="0 0 8 10"><path d="M6 1L2 5l4 4" fill="none" stroke="#999" stroke-width="1.5"/></svg></div>
<div class="slide" style="left:1089px;top:1715px"><svg width="8" height="10" viewBox="0 0 8 10"><path d="M2 1l4 4-4 4" fill="none" stroke="#999" stroke-width="1.5"/></svg></div>

<div class="player" style="left:132px;top:1673px">
  <div class="face" role="img" aria-label="Player portrait in a pink shirt" style="background:radial-gradient(circle at 50% 70%,#f29bc2,#2b2b2b 75%)"></div>
  <svg class="flag" width="20" height="13" viewBox="0 0 20 13"><rect width="20" height="13" fill="#c8102e"/><rect y="2" width="20" height="2" fill="#fff"/><rect y="6" width="20" height="2" fill="#fff"/><rect y="10" width="20" height="2" fill="#fff"/><rect width="9" height="7" fill="#1f3b7a"/></svg>
  <div class="pname">OWEN HARTLEY</div>
  <div class="pcopy">Lorem ipsum dolor sit amet, co ctetuer adipiscing elit, sed dia.</div>
  <div class="pct">7.42%</div>
</div>
<div class="player" style="left:455px;top:1673px">
  <div class="face" role="img" aria-label="Player portrait in a light shirt" style="background:radial-gradient(circle at 50% 70%,#e8eef2,#9aa6ae 75%)"></div>
  <svg class="flag" width="20" height="13" viewBox="0 0 20 13"><rect width="20" height="13" fill="#c8102e"/><rect y="2" width="20" height="2" fill="#fff"/><rect y="6" width="20" height="2" fill="#fff"/><rect y="10" width="20" height="2" fill="#fff"/><rect width="9" height="7" fill="#1f3b7a"/></svg>
  <div class="pname">OWEN HARTLEY</div>
  <div class="pcopy">Lorem ipsum dolor sit amet, co ctetuer adipiscing elit, sed dia.</div>
  <div class="pct">7.42%</div>
</div>
<div class="player" style="left:778px;top:1673px">
  <div class="face" role="img" aria-label="Player portrait in a white shirt" style="background:radial-gradient(circle at 50% 70%,#f4f4f4,#222 75%)"></div>
  <svg class="flag" width="20" height="13" viewBox="0 0 20 13"><rect width="20" height="13" fill="#c8102e"/><rect y="2" width="20" height="2" fill="#fff"/><rect y="6" width="20" height="2" fill="#fff"/><rect y="10" width="20" height="2" fill="#fff"/><rect width="9" height="7" fill="#1f3b7a"/></svg>
  <div class="pname">OWEN HARTLEY</div>
  <div class="pcopy">Lorem ipsum dolor sit amet, co ctetuer adipiscing elit, sed dia.</div>
  <div class="pct">7.42%</div>
</div>

<div class="rule" style="left:131px;top:1835px;width:937px"></div>

<div class="tab on" style="left:131px;top:1871px;width:109px">EVERTHING</div>
<div class="tab" style="left:245px;top:1871px;width:110px">ALL VIDEOS</div>
<div class="tab" style="left:360px;top:1871px;width:94px">SOCIALS</div>

<div class="vcard" style="left:132px;top:1941px">
  <div class="pic" role="img" aria-label="Golfer splashing out of a sand trap" style="background:linear-gradient(180deg,#8ea860,#c7b088)"><svg class="play" width="40" height="40" viewBox="0 0 40 40"><circle cx="20" cy="20" r="17" fill="none" stroke="#fff" stroke-width="2.5"/><path d="M16 12l11 8-11 8z" fill="#fff"/></svg></div>
  <div class="cap">Round RecapsMartin Ellery<br>scards.</div><div class="meta">Fine form at Cedarbrook</div>
</div>
<div class="vcard" style="left:374px;top:1941px">
  <div class="pic" role="img" aria-label="Two golfers walking on the fairway" style="background:linear-gradient(180deg,#b7c27a,#4f9a34)"><svg class="play" width="40" height="40" viewBox="0 0 40 40"><circle cx="20" cy="20" r="17" fill="none" stroke="#fff" stroke-width="2.5"/><path d="M16 12l11 8-11 8z" fill="#fff"/></svg></div>
  <div class="cap">Round RecapsMartin Ellery<br>scards.</div><div class="meta">Fine form at Cedarbrook</div>
</div>
<div class="vcard" style="left:616px;top:1941px">
  <div class="pic" role="img" aria-label="Golfers on a bright green course" style="background:linear-gradient(180deg,#a3c86a,#5aa032)"><svg class="play" width="40" height="40" viewBox="0 0 40 40"><circle cx="20" cy="20" r="17" fill="none" stroke="#fff" stroke-width="2.5"/><path d="M16 12l11 8-11 8z" fill="#fff"/></svg></div>
  <div class="cap">Round RecapsMartin Ellery<br>scards.</div><div class="meta">Fine form at Cedarbrook</div>
</div>
<div class="vcard" style="left:858px;top:1941px">
  <div class="pic" role="img" aria-label="Golfer addressing the ball near a resort" style="background:linear-gradient(180deg,#6fa6dc 0%,#a9c6a0 45%,#4e8f2c 100%)"><svg class="play" width="40" height="40" viewBox="0 0 40 40"><circle cx="20" cy="20" r="17" fill="none" stroke="#fff" stroke-width="2.5"/><path d="M16 12l11 8-11 8z" fill="#fff"/></svg></div>
  <div class="cap">Round RecapsMartin Ellery<br>scards.</div><div class="meta">Fine form at Cedarbrook</div>
</div>

<section class="partners">
  <h2 class="section-title" style="top:26px">OUR&nbsp; PARTNERS</h2>
  <div class="badge" style="left:136px;top:79px;width:88px;height:88px;border-radius:50%;background:#d9d9d9"></div>
  <div class="badge" style="left:282px;top:92px;width:200px;height:58px;background:#eaeaea"></div>
  <div class="badge" style="left:552px;top:80px;width:114px;height:86px;border-radius:8px;background:#e4f1dc"></div>
  <div class="badge" style="left:741px;top:78px;width:114px;height:86px;border-radius:8px;background:#e4f1dc"></div>
  <div class="badge" style="left:930px;top:78px;width:114px;height:88px;background:#2f8fd0"></div>
</section>

<footer class="footer">
  <div class="links"><a>DISCLAIMER</a><a>TERMS &amp; CONDITIONS</a></div>
  <div class="copy">(C) ALL COPYRIGHTS ARE RESERVED 2014</div>
  <div class="social"><span></span><span></span><span></span><span></span></div>
  <div class="brand-foot" style="left:965px"><span class="dot"></span>Fairway Circuit</div>
</footer>

</body>
</html>
```